Audio Visual & Broadcast Installing Company needs a Web Site Design

We need a website design for our company Halvern Crane Ltd. We are a small company that does Audio Visual and broadcast installations. We are looking to expand our business and need a professional web presence. All work completed by us is done to a very high standard and it’s this attention to detail that sets us apart from our competitors. Our projects include doing fibre optics at major sporting events; installing and commissioning bespoke control systems on super yachts and installing the latest systems in luxury homes.

We provide the following services:
System design
On-site installation
Rack building
Pre-fabricated cable looms
Fibre optic cabling

We would like a website that gives details of our services and provides contact information. Our customers are other businesses and our website needs to reflect this. The flyer attached will be used to promote the company and we would like the website to follow this theme. Please use the colours from our logo, as the colour scheme. We know that our colours are bright and we don’t want them to overwhelm the site. With our website we want to communicate that we are professional and provide a quality service.
NB UPDATE: please use stock images for any graphical elements.

The following 3 sites belong to some of our competitors. The first 2, we DON'T like because they don't project a professional feeling. The last one, 'lumatrexlinks', is better as it provides the required information in a clear, simple form.

http://www.qorvamedia.example/

http://www.pellisforthwiring.example/

http://www.lumatrexlinks.example/

We really like the following site, it feels professional and high end without too many flashy graphics. We want something that is fast to load but still shows the high end quality of our work.

http://oberlyncraft.example/

Pages/Sections

Home
On site installation
Rack building and cable looms
Fibre optics
Portfolio (this will be limited to start with but must be easy to expand and add new projects)
Updates

Target Market(s)

Businesses operating in the following areas:
Audio Vision, Broadcasting, Home Automation, Events

Industry/Entity Type

Broadcasting

Coding

Coded - Design and coding required

Number of Pages Required

4 page

Font styles to use
Other font styles liked:
• similar to attached flyer

Requirements
Must have
• The same theme as the 'flyer1' attachment.

```html
<!DOCTYPE html>
<html lang="en">
<head>
<meta charset="utf-8">
<title>Halvern Crane – Audio Visual Installations</title>
<link rel="stylesheet" href="https://fonts.googleapis.com/css2?family=Roboto:wght@400;500;700&family=Open+Sans:wght@400;600&display=swap">
<style>
:root{
  --blue:#1d6ff0;
  --blue-dark:#0f4fc4;
  --red:#e3123f;
  --ink:#222;
  --text:#555;
  --light:#f3f3f4;
  --footer:#f6f6f6;
  --white:#fff;
}
*{box-sizing:border-box;margin:0;padding:0}
html,body{width:1200px;height:3536px;overflow:hidden}
body{position:relative;font-family:"Open Sans",sans-serif;color:var(--text);background:var(--white)}
.abs{position:absolute}
h1,h2,h3,h4{font-family:"Roboto",sans-serif}
.btn{position:absolute;background:var(--blue);color:#fff;font:700 13px "Roboto",sans-serif;text-transform:uppercase;display:flex;align-items:center;justify-content:center;letter-spacing:.3px}

/* hero */
.hero{position:absolute;left:0;top:0;width:1200px;height:700px;overflow:hidden}
.hero-photo{position:absolute;inset:0;background:radial-gradient(ellipse at 75% 30%,#6b5a6a 0%,#3a3540 35%,#1e1e24 70%),#222}
.hero-shade{position:absolute;inset:0;background:linear-gradient(90deg,rgba(0,0,0,.55),rgba(0,0,0,.15))}
.brand{position:absolute;display:flex;align-items:center;gap:10px;font:700 30px "Roboto",sans-serif}
.brand .mark{width:26px;height:26px;background:var(--red)}
.brand-top{left:100px;top:70px;color:#fff}
.phone{left:605px;top:48px;color:#fff;font:400 20px "Roboto",sans-serif;display:flex;gap:12px;align-items:center}
.search{left:884px;top:46px;width:216px;height:30px;border-radius:15px;background:#fff;font-size:11px;color:#777;padding:8px 14px;display:flex;justify-content:space-between}
.nav{left:330px;top:106px;display:flex;gap:27px;color:#fff;font:700 13px "Roboto",sans-serif;text-transform:uppercase}
.hero-kicker{left:98px;top:258px;color:#fff;font:500 42px "Roboto",sans-serif}
.hero-title{left:98px;top:300px;color:#fff;font:500 56px "Roboto",sans-serif}
.hero-copy{left:98px;top:370px;width:380px;color:#fff;font-size:15px;line-height:22px}
.hero-btn{left:98px;top:432px;width:127px;height:34px}
.dots{left:100px;top:494px;display:flex;gap:6px}
.dots span{width:12px;height:12px;border-radius:50%;border:2px solid #fff}
.dots span.on{background:#fff}

/* welcome */
.welcome-frame{left:104px;top:793px;width:383px;height:354px;background:var(--blue)}
.welcome-photo{left:112px;top:800px;width:375px;height:350px;background:linear-gradient(135deg,#5a6a7a,#8ea0ae 45%,#3d4a55)}
.section-title{font:700 30px "Roboto",sans-serif;color:var(--ink);text-transform:uppercase}
.welcome-title{left:533px;top:820px}
.welcome-copy{left:533px;top:878px;width:570px;font-size:12.5px;line-height:22px}
.welcome-copy p+p{margin-top:14px}
.welcome-btn{left:533px;top:1083px;width:110px;height:32px;font-size:12px}

/* services */
.services{left:0;top:1255px;width:1200px;height:556px;background:var(--light)}
.services-title{left:0;top:1322px;width:1200px;text-align:center}
.service{position:absolute;width:330px;height:130px}
.service svg{position:absolute;left:0;top:0}
.service h3{position:absolute;left:120px;top:0;font:400 19px "Roboto",sans-serif;color:var(--ink)}
.service p{position:absolute;left:120px;top:34px;width:180px;font-size:12px;line-height:22px}

/* broadcast */
.broadcast{left:0;top:1811px;width:1200px;height:455px;background:var(--blue)}
.broadcast-photo{left:0;top:1811px;width:640px;height:455px;clip-path:polygon(0 0,100% 0,550px 100%,0 100%);background:linear-gradient(180deg,#4c8fd6 0%,#9ec3e6 40%,#3a4a66 70%,#1a2233 100%)}
.broadcast-title{left:690px;top:1920px;color:#fff;font:500 36px "Roboto",sans-serif;line-height:44px}
.broadcast-copy{left:690px;top:2022px;width:410px;color:#fff;font-size:12px;line-height:22px}
.broadcast-copy p+p{margin-top:16px}

/* news */
.news-title{left:0;top:2330px;width:1200px;text-align:center}
.news-card{position:absolute;width:316px;height:340px}
.news-img{width:316px;height:185px}
.news-date{position:absolute;left:0;top:210px;width:56px;height:75px;background:linear-gradient(180deg,var(--red),var(--blue));color:#fff;text-align:center;font:700 10px "Roboto",sans-serif;padding-top:8px}
.news-date b{display:block;font:500 22px "Roboto",sans-serif;margin-top:3px}
.news-card h4{position:absolute;left:80px;top:205px;width:230px;font:400 16px "Roboto",sans-serif;color:var(--ink);text-transform:uppercase;line-height:21px}
.news-card p{position:absolute;left:80px;top:255px;width:230px;font-size:11px;line-height:20px}

/* testimonial */
.testimonial{left:0;top:2806px;width:1200px;height:365px;background:linear-gradient(90deg,#e01040 0%,#b8155a 35%,#5a3fd0 65%,#1f6ef0 100%)}
.quote-mark{left:178px;top:2905px;color:#fff;font:700 72px "Roboto",sans-serif}
.testi-photo{left:137px;top:2932px;width:124px;height:124px;border-radius:50%;border:5px solid #fff;background:linear-gradient(160deg,#d9c2ad,#8a6c58)}
.testi-title{left:307px;top:2875px;color:#fff;font:500 28px "Roboto",sans-serif}
.testi-rule{left:285px;top:2932px;width:2px;height:110px;background:#fff}
.testi-copy{left:307px;top:2930px;width:760px;color:#fff;font:italic 400 15px "Open Sans",sans-serif;line-height:24px}
.testi-name{left:307px;top:3032px;color:#fff;font:italic 700 15px "Open Sans",sans-serif}
.testi-dots{left:313px;top:3097px;display:flex;gap:6px}
.testi-dots span{width:24px;height:3px;background:rgba(255,255,255,.5)}
.testi-dots span.on{background:#fff}

/* footer */
.footer{left:0;top:3171px;width:1200px;height:305px;background:var(--footer)}
.brand-foot{left:118px;top:3265px;color:var(--ink);font-size:26px}
.socials{left:128px;top:3365px;display:flex;gap:6px}
.socials span{width:24px;height:24px;border-radius:50%;border:1.5px solid #333}
.foot-h{font:500 18px "Roboto",sans-serif;color:var(--ink);text-transform:uppercase}
.foot-news{left:343px;top:3222px}
.foot-news p{font-size:11px;line-height:19px;width:200px;margin-top:28px}
.email{left:343px;top:3319px;width:248px;height:38px;border:1px solid #ddd;background:#fff;font-size:11px;color:#888;padding:11px 12px}
.signup{left:343px;top:3372px;width:124px;height:30px;font-size:12px}
.foot-contact{left:655px;top:3222px}
.contact-line{position:absolute;left:680px;font-size:12px;line-height:18px;color:#555}
.contact-ico{position:absolute;left:655px}
.foot-links{left:930px;top:3222px}
.foot-links ul{list-style:none;margin-top:26px;font-size:12px;line-height:22px}
.copyright{left:0;top:3476px;width:1200px;height:60px;background:#fff;text-align:center;font-size:12px;line-height:60px;color:#333;border-top:1px solid #e5e5e5}
</style>
</head>
<body>

<!-- hero -->
<section class="hero">
  <div class="hero-photo" role="img" aria-label="Sound engineer at a mixing console during a live outdoor concert"></div>
  <div class="hero-shade"></div>
  <svg class="abs" style="left:0;top:0" width="1200" height="700" aria-hidden="true">
    <polygon points="0,620 600,690 1200,620 1200,700 0,700" fill="#fff"/>
    <polyline points="0,620 600,690 1200,620" fill="none" stroke="#1d6ff0" stroke-width="6"/>
  </svg>
</section>
<div class="brand brand-top"><span class="mark"></span>Halvern Crane</div>
<div class="abs phone">
  <svg width="22" height="22" viewBox="0 0 24 24"><path fill="#fff" d="M6.6 10.8a15 15 0 0 0 6.6 6.6l2.2-2.2c.3-.3.7-.4 1-.2 1.1.4 2.3.6 3.6.6.6 0 1 .4 1 1V20c0 .6-.4 1-1 1A17 17 0 0 1 3 4c0-.6.4-1 1-1h3.5c.6 0 1 .4 1 1 0 1.3.2 2.5.6 3.6.1.3 0 .7-.2 1z"/></svg>
  Call Us : 07700 900 418
</div>
<div class="abs search"><span>search</span>
  <svg width="12" height="12" viewBox="0 0 12 12"><circle cx="5" cy="5" r="3.6" fill="none" stroke="#333" stroke-width="1.6"/><line x1="7.6" y1="7.6" x2="11" y2="11" stroke="#333" stroke-width="1.6"/></svg>
</div>
<nav class="abs nav"><span>Home</span><span>On site installation</span><span>Rack building and cable looms</span><span>Fibre optics</span><span>Portfolio</span><span>Contact us</span></nav>
<h2 class="abs hero-kicker">AUDIO VISUAL</h2>
<h1 class="abs hero-title">INSTALLATIONS</h1>
<p class="abs hero-copy">Sed ut perspiciatis unde omnis iste natus voluptatem accusantium doloremque laudantium, totam</p>
<div class="btn hero-btn">Learn more</div>
<div class="abs dots"><span class="on"></span><span></span><span></span></div>

<!-- welcome -->
<div class="abs welcome-frame"></div>
<div class="abs welcome-photo" role="img" aria-label="Technician in a hard hat wiring an electrical control cabinet"></div>
<h2 class="abs section-title welcome-title">Welcome to Halvern Crane</h2>
<div class="abs welcome-copy">
  <p>Sed ut perspiciatis unde omnis iste natus error sit voluptatem accusantium doloremque laudantium, totam rem aperiam, eaque ipsa quae ab illo inventore veritatis et quasi architecto beatae vitae dicta sunt explicabo. Nemo enim ipsam voluptatem quia voluptas sit aspernatur aut odit aut fugit, sed quia consequuntur magni dolores eos qui ratione voluptatem sequi nesciunt.</p>
  <p>Lorem ipsum dolor sit amet, consectetur adipiscing elit, sed do eiusmod tempor incididunt ut labore et dolore magna aliqua. Ut enim ad minim veniam, quis nostrud exercitation ullamco laboris nisi ut aliquip ex ea commodo consequat. Duis aute irure dolor in reprehenderit</p>
</div>
<div class="btn welcome-btn">Read more</div>

<!-- services -->
<div class="abs services"></div>
<h2 class="abs section-title services-title">Our services</h2>

<div class="service" style="left:95px;top:1418px">
  <svg width="100" height="110" viewBox="0 0 100 110"><polygon points="50,2 96,28 96,82 50,108 4,82 4,28" fill="#e3123f"/><polygon points="50,10 89,32 89,78 50,100 11,78 11,32" fill="none" stroke="#fff" stroke-width="1.5" opacity=".5"/><rect x="32" y="40" width="36" height="24" rx="2" fill="none" stroke="#fff" stroke-width="3"/><rect x="26" y="66" width="48" height="4" fill="#fff"/></svg>
  <h3>System design</h3><p>Sed ut perspiciatis unde omnis iste natus error sit voluptatem accusantium doloremque totam rem</p>
</div>
<div class="service" style="left:450px;top:1418px">
  <svg width="100" height="110" viewBox="0 0 100 110"><polygon points="50,2 96,28 96,82 50,108 4,82 4,28" fill="#e3123f"/><polygon points="50,10 89,32 89,78 50,100 11,78 11,32" fill="none" stroke="#fff" stroke-width="1.5" opacity=".5"/><line x1="34" y1="72" x2="58" y2="48" stroke="#fff" stroke-width="7" stroke-linecap="round"/><circle cx="63" cy="42" r="10" fill="#fff"/><circle cx="67" cy="38" r="4" fill="#e3123f"/></svg>
  <h3>On-site installation</h3><p>Sed ut perspiciatis unde omnis iste natus error sit voluptatem accusantium doloremque totam rem</p>
</div>
<div class="service" style="left:805px;top:1418px">
  <svg width="100" height="110" viewBox="0 0 100 110"><polygon points="50,2 96,28 96,82 50,108 4,82 4,28" fill="#e3123f"/><polygon points="50,10 89,32 89,78 50,100 11,78 11,32" fill="none" stroke="#fff" stroke-width="1.5" opacity=".5"/><rect x="36" y="32" width="28" height="46" fill="#fff"/><g fill="#e3123f"><rect x="41" y="38" width="7" height="5"/><rect x="52" y="38" width="7" height="5"/><rect x="41" y="48" width="7" height="5"/><rect x="52" y="48" width="7" height="5"/><rect x="41" y="58" width="7" height="5"/><rect x="52" y="58" width="7" height="5"/></g></svg>
  <h3>Rack building</h3><p>Sed ut perspiciatis unde omnis iste natus error sit voluptatem accusantium doloremque totam rem</p>
</div>
<div class="service" style="left:95px;top:1598px">
  <svg width="100" height="110" viewBox="0 0 100 110"><polygon points="50,2 96,28 96,82 50,108 4,82 4,28" fill="#e3123f"/><polygon points="50,10 89,32 89,78 50,100 11,78 11,32" fill="none" stroke="#fff" stroke-width="1.5" opacity=".5"/><rect x="22" y="44" width="36" height="22" fill="#fff"/><g fill="#fff"><rect x="62" y="44" width="4" height="22"/><rect x="70" y="46" width="4" height="18"/><rect x="78" y="48" width="4" height="14"/></g></svg>
  <h3>Pre-fabricated cable</h3><p>Sed ut perspiciatis unde omnis iste natus error sit voluptatem accusantium doloremque totam rem</p>
</div>
<div class="service" style="left:450px;top:1598px">
  <svg width="100" height="110" viewBox="0 0 100 110"><polygon points="50,2 96,28 96,82 50,108 4,82 4,28" fill="#e3123f"/><polygon points="50,10 89,32 89,78 50,100 11,78 11,32" fill="none" stroke="#fff" stroke-width="1.5" opacity=".5"/><path d="M40 32v16c0 14 20 14 20 0V32" fill="none" stroke="#fff" stroke-width="4"/><circle cx="50" cy="66" r="10" fill="none" stroke="#fff" stroke-width="4"/><circle cx="50" cy="66" r="3" fill="#fff"/></svg>
  <h3>Fibre optic cabling</h3><p>Sed ut perspiciatis unde omnis iste natus error sit voluptatem accusantium doloremque totam rem</p>
</div>
<div class="service" style="left:805px;top:1598px">
  <svg width="100" height="110" viewBox="0 0 100 110"><polygon points="50,2 96,28 96,82 50,108 4,82 4,28" fill="#e3123f"/><polygon points="50,10 89,32 89,78 50,100 11,78 11,32" fill="none" stroke="#fff" stroke-width="1.5" opacity=".5"/><polygon points="30,48 42,48 66,34 66,76 42,62 30,62" fill="#fff"/><rect x="40" y="62" width="7" height="14" fill="#fff"/></svg>
  <h3>Audio Visual</h3><p>Sed ut perspiciatis unde omnis iste natus error sit voluptatem accusantium doloremque totam rem</p>
</div>

<!-- broadcast -->
<div class="abs broadcast"></div>
<div class="abs broadcast-photo" role="img" aria-label="Satellite dish overlooking a city skyline at dusk"></div>
<h2 class="abs broadcast-title">BROADCAST &amp; AV SYSTEM<br>INSTALLATION</h2>
<div class="abs broadcast-copy">
  <p>Halvern Crane provide cabling services for the Broadcast and Audio Visual industries. We specialise in the neat and clean installation which has come to be expected on high end systems. This helps us to achieve a robust and easily maintained installation that you can depend on.</p>
  <p>For a quote or to discuss your project email sam@halvern-crane.example or call us on 07700 900 418.</p>
</div>

<!-- news -->
<h2 class="abs section-title news-title">Latest news</h2>
<article class="news-card" style="left:98px;top:2407px">
  <div class="news-img" role="img" aria-label="Rows of blue network cables patched into a server rack" style="background:linear-gradient(135deg,#1b3f8a,#3d6fd0 50%,#101c3a)"></div>
  <div class="news-date">&#9638;<b>25</b>JUNE</div>
  <h4>Sed ut perspiciatis unde omnis iste natus</h4>
  <p>Lorem ipsum dolor sit amet, consectetur adipiscing elit, sed do eiusmod tempor incid-idunt ut labore et dolor</p>
</article>
<article class="news-card" style="left:443px;top:2407px">
  <div class="news-img" role="img" aria-label="Night city with light trails and a connected network overlay" style="background:linear-gradient(135deg,#1a2440,#7a5a3a 50%,#2a3a5a)"></div>
  <div class="news-date">&#9638;<b>25</b>JUNE</div>
  <h4>Sed ut perspiciatis unde omnis iste natus</h4>
  <p>Lorem ipsum dolor sit amet, consectetur adipiscing elit, sed do eiusmod tempor incid-idunt ut labore et dolor</p>
</article>
<article class="news-card" style="left:787px;top:2407px">
  <div class="news-img" role="img" aria-label="Mixing desk in front of a stage at a live event" style="background:linear-gradient(180deg,#6a5048,#3a302c 55%,#1a1816)"></div>
  <div class="news-date">&#9638;<b>25</b>JUNE</div>
  <h4>Sed ut perspiciatis unde omnis iste natus</h4>
  <p>Lorem ipsum dolor sit amet, consectetur adipiscing elit, sed do eiusmod tempor incid-idunt ut labore et dolor</p>
</article>

<!-- testimonial -->
<div class="abs testimonial"></div>
<div class="abs quote-mark" style="top:2860px">&#8221;</div>
<div class="abs testi-photo" role="img" aria-label="Portrait of the client giving the testimonial"></div>
<h2 class="abs testi-title">TESTIMONIAL</h2>
<div class="abs testi-rule"></div>
<p class="abs testi-copy">Sed ut perspiciatis unde omnis iste natus error sit voluptatem accusantium doloremque laudantium, totam rem aperiam, eaque ipsa quae ab illo inventore veritatis et quasi architecto beatae vitae dicta sunt explicabo. Nemo enim ipsam voluptatem quia voluptas sit aspernatur aut odit aut fugit, sed quia consequuntur magni dolores eos qui ratione voluptatem sequi nesciunt. Neque porro quisquam est, qui dolorem ipsum</p>
<p class="abs testi-name">Corra Fielding – Halvern Crane</p>
<div class="abs testi-dots"><span class="on"></span><span></span><span></span></div>

<!-- footer -->
<footer>
  <div class="abs footer"></div>
  <div class="brand brand-foot"><span class="mark" style="width:22px;height:22px"></span>Halvern Crane</div>
  <div class="abs socials"><span></span><span></span><span></span><span></span></div>

  <div class="abs foot-news"><h4 class="foot-h">Sign up for newsletter</h4>
    <p>Excepteur sint occaecat cupidatat non proident, sunt in culpa qui officia deserunt</p></div>
  <div class="abs email">Enter email</div>
  <div class="btn signup">Sign up</div>

  <div class="abs foot-contact"><h4 class="foot-h">Contact us</h4></div>
  <svg class="contact-ico" style="top:3278px" width="14" height="16" viewBox="0 0 14 16"><path d="M7 1a5 5 0 0 0-5 5c0 4 5 9 5 9s5-5 5-9a5 5 0 0 0-5-5z" fill="#444"/><circle cx="7" cy="6" r="2" fill="#f6f6f6"/></svg>
  <div class="contact-line" style="top:3276px">Halvern Crane<br>14 Wexley Parade<br>Marlow Bay NSW 2150</div>
  <svg class="contact-ico" style="top:3347px" width="14" height="14" viewBox="0 0 24 24"><path fill="#444" d="M6.6 10.8a15 15 0 0 0 6.6 6.6l2.2-2.2c.3-.3.7-.4 1-.2 1.1.4 2.3.6 3.6.6.6 0 1 .4 1 1V20c0 .6-.4 1-1 1A17 17 0 0 1 3 4c0-.6.4-1 1-1h3.5c.6 0 1 .4 1 1 0 1.3.2 2.5.6 3.6.1.3 0 .7-.2 1z"/></svg>
  <div class="contact-line" style="top:3345px">Telephone: 07700 900 418</div>
  <svg class="contact-ico" style="top:3381px" width="14" height="11" viewBox="0 0 14 11"><rect width="14" height="11" fill="#444"/><polyline points="0,0 7,6 14,0" fill="none" stroke="#f6f6f6" stroke-width="1.4"/></svg>
  <div class="contact-line" style="top:3377px">Email : sam@halvern-crane.example</div>

  <div class="abs foot-links"><h4 class="foot-h">Quick links</h4>
    <ul><li>Home</li><li>On site installation</li><li>Rack building and cable looms</li><li>Fibre optics</li><li>Portfolio</li><li>Contact us</li></ul></div>

  <div class="abs copyright">©2017 Halvern Crane . All Rights Reserved.</div>
</footer>

</body>
</html>
```